Existing Website Requiring new Pages

I have an existing word press website that was built using elementor.
Website: www.tallowmerecare.com.au
I require the Vacancies page (https://www.tallowmerecare.com.au/vacancies/) to be modified to display our new properties along with minor tweaks to how the information is presented.
The vacancies to be displayed are the exactly the same as those that are located on the homepage of QDA website (https://qda.org.au/)
The new pages that link off the Vacancies tab will require custom design.
There are roughly 8 pages/properties to be incorporated. i wish for the design to be very similar to that displayed in the following link; https://www.zomplex.com.au/vacancies/merrylands
Along with this the back end has not been updated for the last 3 years so it also requires some maintenance.
Website is in the disability industry and the custom pages will display information relative to Property Vacancies.
I have attached a ZIP file with some design guides, the information for each of the properties (which will need to be modified to show our business name Tallowmere Healthcare) and the example of how it is to look based off the Zomplex website.
If you guys have any suggestions or ideas on how to make this more presentable or possible i'm open to your ideas.
People looking for SDA properties custom built for people with a disability
Disability
Coded - Design and coding required
5+ page

```html
<!DOCTYPE html>
<html lang="en">
<head>
<meta charset="utf-8">
<title>Tallowmere Healthcare – Disability Care Vacancies</title>
<link rel="stylesheet" href="https://fonts.googleapis.com/css2?family=Poppins:wght@400;500;600&display=swap">
<style>
:root{
  --orange:#fbbf5f;
  --orange-deep:#f3ab3c;
  --orange-soft:#fcd596;
  --ink:#222222;
  --muted:#7a7a7a;
  --card:#ececec;
  --cream:#fdf1de;
  --white:#ffffff;
  --line:#e6d9c4;
}
*{box-sizing:border-box;margin:0;padding:0}
html,body{width:1200px;height:3732px;overflow:hidden}
body{font-family:'Poppins',sans-serif;color:var(--ink);background:var(--white);position:relative}

/* header */
.site-header{position:absolute;left:0;top:0;width:1200px;height:92px;background:var(--white);border-bottom:1px solid #eee}
.brand{position:absolute;left:120px;top:32px;display:flex;align-items:center;gap:8px;font-weight:500;font-size:17px;color:var(--orange-deep);letter-spacing:.5px}
.brand-dot{width:14px;height:14px;border-radius:50%;background:var(--orange)}
.main-nav{position:absolute;left:330px;top:34px;display:flex;gap:18px;font-size:16px}
.main-nav a{color:var(--ink);text-decoration:none}
.main-nav a.active{text-decoration:underline}
.btn-login{position:absolute;left:983px;top:22px;width:134px;height:48px;border-radius:6px;background:var(--orange-soft);color:var(--white);font-size:17px;font-weight:500;display:flex;align-items:center;justify-content:center}

/* hero */
.hero{position:absolute;left:0;top:92px;width:1200px;height:551px;background:linear-gradient(100deg,#e9b45e 0%,#f3c06a 50%,#efc27a 100%)}
.hero h1{position:absolute;left:0;top:38px;width:1200px;text-align:center;color:var(--white);font-weight:600;font-size:33px;line-height:50px}
.hero p{position:absolute;left:140px;top:150px;width:920px;text-align:center;color:var(--white);font-size:19px;line-height:29px}
.search-bar{position:absolute;left:83px;top:248px;width:1034px;height:95px;background:var(--white);border-radius:8px;box-shadow:0 4px 14px rgba(0,0,0,.12);z-index:2}
.search-field{position:absolute;top:20px;display:flex;align-items:center;gap:14px;font-size:20px}
.search-icon{width:58px;height:55px;border-radius:6px;background:var(--orange-soft);display:flex;align-items:center;justify-content:center}
.btn-search{position:absolute;left:885px;top:23px;width:118px;height:50px;border-radius:6px;background:var(--orange-soft);color:var(--white);font-size:18px;font-weight:500;display:flex;align-items:center;justify-content:center}
.map{position:absolute;left:160px;top:472px;width:880px;height:411px;background:linear-gradient(135deg,#e6e8ea,#d7e9d5 45%,#e9ecef);clip-path:polygon(80px 0,100% 0,100% calc(100% - 130px),calc(100% - 160px) 100%,0 100%,0 80px)}

/* services */
.eyebrow{position:absolute;left:0;top:985px;width:1200px;text-align:center;color:var(--orange-deep);font-weight:500;font-size:23px}
.section-title{position:absolute;left:0;width:1200px;text-align:center;font-weight:500;font-size:30px;line-height:46px}
.section-lead{position:absolute;left:120px;top:1135px;width:960px;text-align:center;color:var(--muted);font-size:19px;line-height:30px}
.service-card{position:absolute;width:509px;height:173px;background:var(--card);clip-path:polygon(50px 0,100% 0,100% calc(100% - 60px),calc(100% - 60px) 100%,0 100%,0 50px)}
.service-icon{position:absolute;left:30px;top:50px;width:70px;height:70px;border-radius:14px;background:var(--orange)}
.service-card h3{position:absolute;left:134px;top:38px;font-weight:500;font-size:24px}
.service-card p{position:absolute;left:134px;top:78px;width:360px;color:var(--muted);font-size:18px;line-height:28px}

/* properties */
.property{position:absolute;width:334px}
.property-photo{width:334px;height:228px;background:linear-gradient(180deg,#cfe2f2 0%,#d9c2a8 45%,#8fa277 75%,#a8a29a 100%);clip-path:polygon(60px 0,100% 0,100% calc(100% - 40px),calc(100% - 60px) 100%,0 100%,0 40px)}
.badge{position:absolute;top:250px;left:0;background:var(--orange);color:var(--white);font-size:12px;font-weight:500;padding:2px 8px;border-radius:4px}
.property h4{position:absolute;top:292px;left:0;font-weight:500;font-size:21px}
.property p{position:absolute;top:328px;left:0;width:330px;color:var(--muted);font-size:18px;line-height:28px}
.tags{position:absolute;top:430px;left:0;display:flex;gap:10px}
.tag{font-size:12px;border:1px solid #ddd;border-radius:4px;padding:2px 7px}

/* contact */
.contact-photo{position:absolute;left:83px;top:2785px;width:435px;height:467px;border-radius:6px;background:linear-gradient(135deg,#9bbf7a,#e8ece6 55%,#c9d7ea)}
.contact-form{position:absolute;left:545px;top:2785px;width:572px;height:467px;border-radius:8px;background:var(--orange)}
.field{position:absolute;color:var(--white);font-size:20px;border-bottom:1.5px solid var(--white);padding-bottom:6px}
.btn-submit{position:absolute;left:25px;top:332px;width:160px;height:50px;border:1.5px solid var(--white);border-radius:8px;color:var(--white);font-size:17px;font-weight:500;display:flex;align-items:center;justify-content:center}

/* footer */
.site-footer{position:absolute;left:0;top:3335px;width:1200px;height:397px;background:var(--cream)}
.footer-brand{position:absolute;left:117px;top:80px;display:flex;align-items:center;gap:8px;font-weight:500;font-size:17px;color:var(--orange-deep)}
.footer-info{position:absolute;left:83px;top:140px;width:380px;color:var(--muted);font-size:18px;line-height:26px}
.footer-info p{margin-bottom:19px}
.footer-col{position:absolute;top:65px;font-size:18px;color:var(--muted)}
.footer-col h5{color:var(--orange-deep);font-weight:600;font-size:21px;margin-bottom:14px}
.footer-col li{list-style:none;margin-bottom:12px}
.footer-rule{position:absolute;left:83px;top:325px;width:1034px;height:1px;background:var(--line)}
.footer-legal{position:absolute;left:0;top:345px;width:1200px;text-align:center;color:var(--muted);font-size:19px}
</style>
</head>
<body>

<header class="site-header">
  <div class="brand"><span class="brand-dot"></span>TALLOWMERE</div>
  <nav class="main-nav">
    <a class="active" href="#">Home</a><a href="#">About us</a><a href="#">What we do</a><a href="#">Referrals</a><a href="#">Feedback</a><a href="#">Contact us</a>
  </nav>
  <div class="btn-login">Login</div>
</header>

<section class="hero" role="img" aria-label="Warm orange-toned photo of a care setting">
  <h1>Welcome to Tallowmere<br>Disability Care Vacancies</h1>
  <p>we specialize in providing compassionate and professional disability care services. With a deep commitment to enhancing the lives of individuals with disabilities</p>
  <div class="search-bar">
    <div class="search-field" style="left:28px">
      <div class="search-icon"><svg width="28" height="30" viewBox="0 0 28 30"><path d="M14 2a9 9 0 0 0-9 9c0 7 9 15 9 15s9-8 9-15a9 9 0 0 0-9-9z" fill="none" stroke="#fff" stroke-width="2.5"/><circle cx="14" cy="11" r="3.5" fill="#fff"/></svg></div>
      Location <svg width="16" height="10" viewBox="0 0 16 10"><path d="M2 2l6 6 6-6" fill="none" stroke="#222" stroke-width="2.2"/></svg>
    </div>
    <div class="search-field" style="left:296px">
      <div class="search-icon"><svg width="30" height="28" viewBox="0 0 30 28"><rect x="4" y="8" width="9" height="18" fill="#fff"/><rect x="15" y="3" width="11" height="23" fill="#fff"/></svg></div>
      City <svg width="16" height="10" viewBox="0 0 16 10"><path d="M2 2l6 6 6-6" fill="none" stroke="#222" stroke-width="2.2"/></svg>
    </div>
    <div class="search-field" style="left:518px">
      <div class="search-icon"><svg width="30" height="28" viewBox="0 0 30 28"><path d="M15 3L3 14h4v11h16V14h4z" fill="#fff"/></svg></div>
      Type of Home <svg width="16" height="10" viewBox="0 0 16 10"><path d="M2 2l6 6 6-6" fill="none" stroke="#222" stroke-width="2.2"/></svg>
    </div>
    <div class="btn-search">Search</div>
  </div>
</section>

<div class="map" role="img" aria-label="Street map showing property locations"></div>

<div class="eyebrow">Our Service</div>
<h2 class="section-title" style="top:1030px">Service providers and SDA investors to<br>create a place to call home</h2>
<p class="section-lead">We are a registered not-for-profit charity, registered NDIS provider and experts in SDA housing requirements. We can help you through every step of the SDA process.</p>

<div class="service-card" style="left:83px;top:1233px"><div class="service-icon" role="img" aria-label="Care plan icon"></div><h3>Personalized Care Plans</h3><p>Tailored to meet the unique needs and preferences of each individual</p></div>
<div class="service-card" style="left:608px;top:1233px"><div class="service-icon" role="img" aria-label="Assistance icon"></div><h3>Daily Living Assistance</h3><p>Help with personal care, meal preparation, and household tasks</p></div>
<div class="service-card" style="left:83px;top:1435px"><div class="service-icon" role="img" aria-label="Healthcare icon"></div><h3>Healthcare Coordination</h3><p>Coordination with healthcare providers and medication management</p></div>
<div class="service-card" style="left:608px;top:1435px"><div class="service-icon" role="img" aria-label="Community icon"></div><h3>Social Engagement</h3><p>Support for community involvement and social activities</p></div>

<h2 class="section-title" style="top:1683px">Browse More Properties</h2>

<article class="property" style="left:83px;top:1762px"><div class="property-photo" role="img" aria-label="Brick house with garage"></div><span class="badge">Available</span><h4>SDA in Greystanes</h4><p>Coming soon. Luxury living in the heart of Blacktown with a designer rooftop garden</p><div class="tags"><span class="tag">1 Bed</span><span class="tag">1 Bath</span><span class="tag">1 Car Space</span></div></article>
<article class="property" style="left:433px;top:1762px"><div class="property-photo" role="img" aria-label="Brick house with paved driveway"></div><span class="badge">Available</span><h4>SDA in Greystanes</h4><p>Coming soon. Luxury living in the heart of Blacktown with a designer rooftop garden</p><div class="tags"><span class="tag">1 Bed</span><span class="tag">1 Bath</span><span class="tag">1 Car Space</span></div></article>
<article class="property" style="left:783px;top:1762px"><div class="property-photo" role="img" aria-label="Single-storey house front"></div><span class="badge">Available</span><h4>SDA in Greystanes</h4><p>Coming soon. Luxury living in the heart of Blacktown with a designer rooftop garden</p><div class="tags"><span class="tag">1 Bed</span><span class="tag">1 Bath</span><span class="tag">1 Car Space</span></div></article>
<article class="property" style="left:83px;top:2245px"><div class="property-photo" role="img" aria-label="Brick house with paved driveway"></div><span class="badge">Available</span><h4>SDA in Greystanes</h4><p>Coming soon. Luxury living in the heart of Blacktown with a designer rooftop garden</p><div class="tags"><span class="tag">1 Bed</span><span class="tag">1 Bath</span><span class="tag">1 Car Space</span></div></article>
<article class="property" style="left:433px;top:2245px"><div class="property-photo" role="img" aria-label="Single-storey house front"></div><span class="badge">Available</span><h4>SDA in Greystanes</h4><p>Coming soon. Luxury living in the heart of Blacktown with a designer rooftop garden</p><div class="tags"><span class="tag">1 Bed</span><span class="tag">1 Bath</span><span class="tag">1 Car Space</span></div></article>
<article class="property" style="left:783px;top:2245px"><div class="property-photo" role="img" aria-label="Brick house with garage"></div><span class="badge">Available</span><h4>SDA in Greystanes</h4><p>Coming soon. Luxury living in the heart of Blacktown with a designer rooftop garden</p><div class="tags"><span class="tag">1 Bed</span><span class="tag">1 Bath</span><span class="tag">1 Car Space</span></div></article>

<div class="contact-photo" role="img" aria-label="Photo of a carer with an elderly woman outdoors"></div>
<form class="contact-form">
  <div class="field" style="left:23px;top:80px;width:229px">First Name</div>
  <div class="field" style="left:283px;top:80px;width:229px">Last Name</div>
  <div class="field" style="left:23px;top:172px;width:489px">Email</div>
  <div class="field" style="left:23px;top:250px;width:489px">Phone number</div>
  <div class="btn-submit">Submit Now</div>
</form>

<footer class="site-footer">
  <div class="footer-brand"><span class="brand-dot"></span>TALLOWMERE</div>
  <div class="footer-info">
    <p>Operating Hours: 9AM To 5PM Monday – Friday</p>
    <p>Phone: +61 0400 318 562</p>
    <p>Email: info@tallowmerecare.com.au</p>
  </div>
  <div class="footer-col" style="left:500px"><h5>Pathers With Us</h5><ul><li>See Our Partners</li><li>Explore Custom Kits</li><li>Explore Custom Kits</li></ul></div>
  <div class="footer-col" style="left:720px"><h5>Support</h5><ul><li>Customer Support</li><li>Technical Assistance</li><li>Press &amp; Media</li></ul></div>
  <div class="footer-col" style="left:978px"><h5>Contact</h5><ul><li>Exam Request</li><li>Locations</li><li>FAQ</li></ul></div>
  <div class="footer-rule"></div>
  <div class="footer-legal">All Right Reserved / Privacy Policy / Terms and Conditions</div>
</footer>

</body>
</html>
```